Presentation Folder with inside Pockets

We need a Presentation Folder with inside pockets. The size of the folder will be 9" x 12" and will be printed on the cover, the back and the inside folder flaps. The design will be very simple and consist of our logo (large) on the front cover and our logo (smaller) and contact information on the back. We are open to various colors that you think may go along with our logo. When you display your work, show the front, back and inside.

Target Market(s)

Pharmaceutical Companies

Industry/Entity Type

Work

Requirements
Should not have
• please do not add stock medical photos.

```html
<!DOCTYPE html>
<html lang="en">
<head>
<meta charset="utf-8">
<title>Veltora Research – Presentation Folder Layout</title>
<link rel="stylesheet" href="https://fonts.googleapis.com/css2?family=Arimo:wght@400;700&display=swap">
<style>
  :root {
    --paper: #ffffff;
    --green-light: #84c64a;
    --green: #6aa83e;
    --blue-light: #1a8fcc;
    --blue: #0a6fae;
    --blue-deep: #0b4f87;
    --dieline: #e0262b;
    --fold: #6fbf73;
    --ink: #1a1a1a;
  }
  html, body {
    margin: 0;
    padding: 0;
    width: 1200px;
    height: 1080px;
    overflow: hidden;
    background: var(--paper);
  }
  .folder-layout {
    display: block;
    width: 1200px;
    height: 1080px;
  }
  .brand-name {
    font-family: "Arimo", Arial, sans-serif;
    font-weight: 700;
    fill: var(--ink);
    letter-spacing: 0.04em;
  }
  .brand-name--reverse { fill: var(--paper); }
  .contact-block {
    font-family: "Arimo", Arial, sans-serif;
    font-weight: 400;
    font-size: 10.5px;
    fill: var(--ink);
    text-anchor: middle;
  }
  .dieline { fill: none; stroke: var(--dieline); stroke-width: 1; }
  .fold-line { fill: none; stroke: var(--fold); stroke-width: 1; }
  .card-slot { fill: var(--paper); }
  .slot-cut { stroke: var(--dieline); stroke-width: 1.2; }
</style>
</head>
<body>
<svg class="folder-layout" viewBox="0 0 1200 1080" xmlns="http://www.w3.org/2000/svg">
  <defs>
    <linearGradient id="greenTone" x1="0" y1="0" x2="1" y2="1">
      <stop offset="0" stop-color="#84c64a"/>
      <stop offset="1" stop-color="#66a63c"/>
    </linearGradient>
    <linearGradient id="blueToneLeft" x1="0" y1="0" x2="1" y2="1">
      <stop offset="0" stop-color="#0b4f87"/>
      <stop offset="1" stop-color="#0a78b8"/>
    </linearGradient>
    <linearGradient id="blueToneRight" x1="0" y1="0" x2="1" y2="1">
      <stop offset="0" stop-color="#0a6fae"/>
      <stop offset="1" stop-color="#1a8fcc"/>
    </linearGradient>
  </defs>

  <!-- Back cover colour field -->
  <rect class="back-cover-field" role="img" aria-label="Decorative green colour field on back cover"
        x="50" y="600" width="549" height="180" fill="url(#greenTone)"/>

  <!-- Front cover colour field -->
  <rect class="front-cover-field" role="img" aria-label="Decorative blue colour field on front cover"
        x="599" y="640" width="548" height="140" fill="url(#blueToneRight)"/>

  <!-- Pocket colour fields -->
  <path class="pocket-field pocket-field--left" role="img" aria-label="Decorative blue colour field on left pocket"
        fill="url(#blueToneLeft)" d="M50,780 L597,780 L570,1025 L50,1025 Z"/>
  <path class="pocket-field pocket-field--right" role="img" aria-label="Decorative blue colour field on right pocket"
        fill="url(#blueToneRight)" d="M603,780 L1147,780 L1147,1025 L630,1025 Z"/>

  <!-- Business card slots -->
  <g class="card-slots">
    <rect class="card-slot" x="203" y="840" width="214" height="123"/>
    <line class="slot-cut" x1="203" y1="860" x2="231" y2="832"/>
    <line class="slot-cut" x1="391" y1="970" x2="424" y2="937"/>
    <rect class="card-slot" x="785" y="840" width="213" height="123"/>
    <line class="slot-cut" x1="777" y1="866" x2="811" y2="832"/>
    <line class="slot-cut" x1="972" y1="970" x2="1005" y2="937"/>
  </g>

  <!-- Fold lines -->
  <line class="fold-line" x1="599" y1="47" x2="599" y2="780"/>
  <line class="fold-line" x1="50" y1="780" x2="1147" y2="780"/>

  <!-- Dieline -->
  <path class="dieline" d="M50,540 L50,47 L1147,47 L1147,540 L1193,565 L1193,745 L1147,780
                           L1147,1025 L630,1025 L603,780 L597,780 L570,1025 L50,1025 L50,780
                           L7,750 L7,568 L50,540"/>
  <line class="dieline" x1="50" y1="540" x2="50" y2="780"/>
  <line class="dieline" x1="1147" y1="540" x2="1147" y2="780"/>

  <!-- Back cover wordmark -->
  <g class="brand-lockup brand-lockup--back">
    <circle cx="226" cy="367" r="16" fill="var(--green-light)"/>
    <text class="brand-name" x="255" y="370" font-size="15">VELTORA RESEARCH</text>
    <text class="brand-name" x="352" y="383" font-size="11" text-anchor="middle">INC.</text>
  </g>

  <!-- Contact details -->
  <text class="contact-block">
    <tspan x="325" y="633">Veltora Research, Inc.</tspan>
    <tspan x="325" y="645">82 Birchwood Lane</tspan>
    <tspan x="325" y="657">Lakeview, NY 11552</tspan>
    <tspan x="325" y="681">Tel: +1-555-014-2290</tspan>
    <tspan x="325" y="693">Email: hello@veltora.net</tspan>
    <tspan x="325" y="706">Web: www.veltora.net</tspan>
  </text>

  <!-- Front cover wordmark -->
  <g class="brand-lockup brand-lockup--front">
    <circle cx="698" cy="367" r="36" fill="var(--green-light)"/>
    <text class="brand-name" x="750" y="372" font-size="30">VELTORA RESEARCH</text>
    <text class="brand-name" x="916" y="392" font-size="20" text-anchor="middle">INC.</text>
  </g>

  <!-- Pocket flap wordmark (reads when folded) -->
  <g class="brand-lockup brand-lockup--flap" transform="rotate(180 135 996)">
    <circle cx="77" cy="996" r="10" fill="var(--green-light)"/>
    <text class="brand-name brand-name--reverse" x="92" y="997" font-size="9.5">VELTORA RESEARCH</text>
    <text class="brand-name brand-name--reverse" x="150" y="1006" font-size="7" text-anchor="middle">INC.</text>
  </g>
</svg>
</body>
</html>
```